HOT TUB - SPAS service needs an business card

I need an business for my company who his specialise in a maintenance,water treatment and cleaning of Hot Tub - Spas for commercial and residential customers. The company operate mainly in the ski resort of Chamonix, Megève and St Gervais. The final product should communicate pure water, cleanest and professional for luxury property's.
I have upload a logo but any improvement on it is welcome.(color,size, details etc..) or any other idea. Thank you
Company Name: 58 BAINS
My name: Laurent Mazeyrac
Email: lmazey@courrielo.fr
Tel: +33 (0)6 81 52 29 07
Description to be on the card in french(first langage) and in English:
- Spas service
- Entretien, traitement eau, nettoyage.
- Maintenance, water treatment, cleaning.

```html
<!DOCTYPE html>
<html lang="fr">
<head>
<meta charset="utf-8">
<title>58 BAINS – Cartes de visite</title>
<link rel="stylesheet" href="https://fonts.googleapis.com/css2?family=Exo+2:wght@400;500;600&display=swap">
<style>
  :root {
    --spa-blue: #4b97c6;
    --spa-blue-faint: #5ea3cd;
    --card-white: #e4e6e7;
    --grey-faint: #d3d6d8;
    --ink: #5a6168;
    --backdrop: #f3f4f5;
  }
  * { box-sizing: border-box; margin: 0; padding: 0; }
  html, body {
    width: 1200px; height: 1000px; overflow: hidden;
    background: var(--backdrop);
    font-family: "Exo 2", sans-serif;
  }
  .sheet {
    position: relative; width: 1200px; height: 1000px;
    display: flex; flex-direction: column; align-items: center; justify-content: center; gap: 44px;
  }
  .card {
    position: relative; width: 760px; height: 434px; overflow: hidden;
    box-shadow: 0 6px 18px rgba(0,0,0,0.12);
  }

  /* Front */
  .card--front { background: var(--spa-blue); }
  .front-brand {
    position: absolute; left: 0; right: 0; top: 130px;
    display: flex; align-items: center; justify-content: center; gap: 16px;
    color: #fff; font-weight: 600; font-size: 52px; letter-spacing: 1px;
  }
  .brand-mark { width: 34px; height: 34px; border-radius: 50%; background: currentColor; flex: none; }
  .front-decoration {
    position: absolute; left: 430px; top: 250px; width: 230px; height: 150px;
    background: var(--spa-blue-faint); border-radius: 10px;
  }

  /* Back */
  .card--back { background: var(--card-white); color: var(--ink); }
  .back-band {
    position: absolute; left: 0; top: 196px; width: 220px; height: 30px; background: var(--spa-blue);
  }
  .name-pill {
    position: absolute; right: 292px; top: 180px; height: 58px; padding: 0 16px;
    background: var(--spa-blue); border-radius: 10px;
    color: #fff; font-size: 36px; font-weight: 400;
    display: flex; align-items: center; white-space: nowrap;
  }
  .role-pill {
    position: absolute; right: 292px; top: 246px; height: 30px; padding: 0 18px;
    background: var(--spa-blue); border-radius: 8px;
    color: #fff; font-size: 17px; white-space: nowrap;
    display: flex; align-items: center;
  }
  .divider {
    position: absolute; left: 488px; top: 188px; width: 2px; height: 42px; background: var(--spa-blue);
  }
  .contact {
    position: absolute; left: 502px; top: 186px; list-style: none;
    font-size: 13px; line-height: 22px; white-space: nowrap;
  }
  .contact li { display: flex; align-items: center; gap: 8px; }
  .contact svg { width: 13px; height: 13px; fill: var(--spa-blue); flex: none; }
  .services { position: absolute; list-style: none; font-size: 15px; line-height: 22px; white-space: nowrap; }
  .services li { display: flex; align-items: center; gap: 9px; }
  .services li::before {
    content: ""; width: 8px; height: 8px; border-radius: 50%; background: var(--spa-blue); flex: none;
  }
  .services--fr { left: 160px; top: 292px; }
  .services--en { left: 504px; top: 250px; font-size: 14px; }
  .back-brand {
    position: absolute; right: 34px; top: 32px;
    display: flex; align-items: center; gap: 8px;
    color: var(--spa-blue); font-weight: 600; font-size: 22px;
  }
  .back-brand .brand-mark { width: 16px; height: 16px; }
  .back-decoration {
    position: absolute; left: 560px; top: 336px; width: 150px; height: 78px;
    background: var(--grey-faint); border-radius: 8px;
  }
</style>
</head>
<body>
<main class="sheet">
  <section class="card card--front" aria-label="Recto de la carte">
    <div class="front-brand"><span class="brand-mark"></span>58 BAINS</div>
    <div class="front-decoration" role="img" aria-label="Motif décoratif pâle de la marque"></div>
  </section>

  <section class="card card--back" aria-label="Verso de la carte">
    <div class="back-brand"><span class="brand-mark"></span>58 BAINS</div>
    <div class="back-band"></div>
    <div class="back-decoration" role="img" aria-label="Motif décoratif pâle de la marque"></div>
    <h1 class="name-pill">Laurent Mazeyrac</h1>
    <p class="role-pill">Spas Services</p>
    <span class="divider"></span>
    <ul class="contact">
      <li>
        <svg viewBox="0 0 24 24" aria-hidden="true"><path d="M6.6 10.8a15 15 0 0 0 6.6 6.6l2.2-2.2a1 1 0 0 1 1-.25 11.4 11.4 0 0 0 3.6.57 1 1 0 0 1 1 1V20a1 1 0 0 1-1 1A17 17 0 0 1 3 4a1 1 0 0 1 1-1h3.5a1 1 0 0 1 1 1c0 1.25.2 2.45.57 3.57a1 1 0 0 1-.25 1z"/></svg>
        +33 (0)6 81 52 29 07
      </li>
      <li>
        <svg viewBox="0 0 24 24" aria-hidden="true"><path d="M2 5h20v14H2zm2 2v.5l8 5 8-5V7l-8 5z"/></svg>
        lmazey@courrielo.fr
      </li>
    </ul>
    <ul class="services services--en">
      <li>Custom maintenance contract.</li>
      <li>Water treatment, cleaning.</li>
      <li>Guidance.</li>
    </ul>
    <ul class="services services--fr">
      <li>Contrat d'entretien sur mesure.</li>
      <li>Traitement eau, nettoyage.</li>
      <li>Conseils.</li>
    </ul>
  </section>
</main>
</body>
</html>
```